Anzeigengestaltung für Online-Handel mit Edelmetallen
Zielgruppe
Online Handel mit Edelmetallen wie Gold und Silberbarren und Münzen.
Sowie der Ankauf von Gold per Postankauf
Aufgabenstellung
Ich möchte in verschiedenen Tageszeitungen in Deutschland Werbung schalten . Kleine Anzeigen etwas kleiner als Visitenkarten Größe wegen den Kosten.
Logo
Ihr Onlineshop für Edelmetalle
Vergleichen sie unsere Preis
Goldbarren / Falkenthaler
Shop.Wertkontorlo.de

```html
<!DOCTYPE html>
<html lang="de">
<head>
<meta charset="utf-8">
<title>Wertkontor-Lo.de – Ihr Onlineshop für Edelmetalle</title>
<link rel="stylesheet" href="https://fonts.googleapis.com/css2?family=Bebas+Neue&display=swap">
<style>
  :root {
    --paper: #ffffff;
    --ink: #111111;
    --brand-brown: #6b5536;
    --arrow-yellow: #f7c21b;
    --photo-dark: #2a2522;
    --photo-gold: #c98a1e;
    --photo-gold-light: #f3c45a;
    --note-violet: #c9b6df;
    --note-green: #b9d7b0;
    --note-orange: #e9c49a;
    --gold-top: #f6d46a;
    --gold-mid: #c8921c;
    --gold-low: #8a5a10;
  }
  html, body {
    margin: 0;
    padding: 0;
    overflow: hidden;
  }
  .ad {
    position: relative;
    width: 1200px;
    height: 600px;
    background: var(--paper);
    overflow: hidden;
    font-family: "Bebas Neue", "Oswald", sans-serif;
  }
  .hero-photo {
    position: absolute;
    inset: 0;
    background: radial-gradient(ellipse at 30% 45%, var(--photo-gold-light) 0%, var(--photo-gold) 30%, #6b4512 55%, var(--photo-dark) 78%);
    clip-path: polygon(0 0, 720px 0, 205px 600px, 0 600px);
  }
  .growth-arrow {
    position: absolute;
    inset: 0;
  }
  .banknote {
    position: absolute;
    width: 150px;
    height: 78px;
    border-radius: 3px;
    opacity: 0.9;
  }
  .banknote--violet { background: linear-gradient(120deg, var(--note-violet), #e6dcef); }
  .banknote--green  { background: linear-gradient(120deg, var(--note-green), #e1eedb); }
  .banknote--orange { background: linear-gradient(120deg, var(--note-orange), #f3e2cd); }
  .brand-name {
    position: absolute;
    left: 720px;
    width: 430px;
    top: 122px;
    margin: 0;
    text-align: center;
    font-size: 40px;
    letter-spacing: 1px;
    color: var(--brand-brown);
    font-weight: 400;
  }
  .messaging {
    position: absolute;
    left: 680px;
    width: 520px;
    top: 225px;
    text-align: center;
    color: var(--ink);
  }
  .price-compare {
    margin: 0;
    font-size: 36px;
    line-height: 1;
    letter-spacing: 0.5px;
  }
  .headline {
    margin: 30px 0 0;
    font-size: 74px;
    line-height: 1;
    font-weight: 400;
  }
  .headline-metal {
    display: block;
    margin-top: 10px;
    font-size: 86px;
    background: linear-gradient(180deg, var(--gold-top) 0%, var(--gold-mid) 55%, var(--gold-low) 100%);
    -webkit-background-clip: text;
    background-clip: text;
    color: transparent;
  }
  .shop-url {
    margin: 62px 0 0;
    font-size: 46px;
    line-height: 1;
    letter-spacing: 0.5px;
  }
</style>
</head>
<body>
<main class="ad">
  <div class="hero-photo" role="img" aria-label="Foto: glänzende Goldbarren und Falkenthaler-Goldmünzen auf dunklem Grund"></div>

  <svg class="growth-arrow" width="1200" height="600" viewBox="0 0 1200 600" aria-hidden="true">
    <polyline points="195,612 330,468 362,490 468,350 508,372 600,240 640,258 742,104"
              fill="none" stroke="var(--paper)" stroke-width="48" stroke-linejoin="miter"/>
    <polyline points="195,612 330,468 362,490 468,350 508,372 600,240 640,258 742,104"
              fill="none" stroke="var(--arrow-yellow)" stroke-width="30" stroke-linejoin="miter"/>
    <polygon points="812,-6 690,70 792,132" fill="var(--arrow-yellow)"/>
  </svg>

  <div class="banknote banknote--violet" style="left:-20px; top:-10px; transform:rotate(-20deg);" role="img" aria-label="Foto: Euro-Banknote"></div>
  <div class="banknote banknote--violet" style="left:150px; top:-30px; transform:rotate(25deg);" role="img" aria-label="Foto: Euro-Banknote"></div>
  <div class="banknote banknote--violet" style="left:-30px; top:460px; transform:rotate(-15deg);" role="img" aria-label="Foto: Euro-Banknote"></div>
  <div class="banknote banknote--violet" style="left:440px; top:320px; transform:rotate(18deg);" role="img" aria-label="Foto: Euro-Banknote"></div>
  <div class="banknote banknote--violet" style="left:1110px; top:140px; transform:rotate(20deg);" role="img" aria-label="Foto: Euro-Banknote"></div>
  <div class="banknote banknote--green" style="left:1120px; top:370px; transform:rotate(-25deg);" role="img" aria-label="Foto: Euro-Banknote"></div>
  <div class="banknote banknote--green" style="left:520px; top:490px; transform:rotate(12deg);" role="img" aria-label="Foto: Euro-Banknote"></div>
  <div class="banknote banknote--orange" style="left:430px; top:520px; transform:rotate(80deg);" role="img" aria-label="Foto: Euro-Banknote"></div>
  <div class="banknote banknote--violet" style="left:600px; top:520px; transform:rotate(-8deg);" role="img" aria-label="Foto: Euro-Banknote"></div>

  <p class="brand-name">Wertkontor-Lo.de</p>

  <section class="messaging">
    <p class="price-compare">Vergleichen Sie unsere Preis</p>
    <h1 class="headline">Ihr Onlineshop für
      <span class="headline-metal">Edelmetalle</span>
    </h1>
    <p class="shop-url">Shop.Wertkontorlo.de</p>
  </section>
</main>
</body>
</html>
```